Quarrytide Hosting - Direct Mailer / Flyer

We are excited to announce the launch of our new company, Quarrytide Hosting, a premier cohosting facility and data center dedicated to Cryptocurrency Miners. Our website, https://quarrytidehosting.example, provides detailed information about our offerings and showcases the innovative design schemes for the entire project.

Quarrytide Hosting stands out in the industry by offering both GPU Hosting and ASIC Hosting services in our state-of-the-art facility, equipped with an impressive 17 Megawatts of available power. What sets us apart is our unique billing system based on actual metered power usage. We charge $0.08 for ASIC miners and $0.09 for GPU miners, ensuring cost-effectiveness and transparency for our clients.

Our commitment to excellence is evident in our use of cutting-edge technology, top-notch facilities, and strategic partnerships. These elements come together to deliver exceptional solutions tailored for real-world applications in the cryptocurrency space.

As part of our promotional efforts, we are developing a direct mailer/flyer to introduce Quarrytide Hosting to a wider audience. This promotional material will also serve as a handout at events, to potential customers, and more. We welcome creative ideas and suggestions to maximize the versatility of this design and reach diverse target audiences effectively.

For a comprehensive overview of our services and to explore our design concepts, please visit https://quarrytidehosting.example. Quarrytide Hosting is poised to revolutionize the mining industry, and we look forward to partnering with you for success in the digital currency era.

```html
<!DOCTYPE html>
<html lang="en">
<head>
<meta charset="utf-8">
<title>Quarrytide Hosting – Flyer</title>
<link rel="stylesheet" href="https://fonts.googleapis.com/css2?family=Bebas+Neue&family=Montserrat:wght@400;500;600;700&display=swap">
<style>
  :root{
    --stage:#e6e7eb;
    --lavender:#c8cff5;
    --lavender-deep:#a7b0de;
    --royal:#3447e2;
    --royal-soft:#5565ee;
    --night:#0b0e24;
    --navy:#0a1160;
    --teal:#1e6a72;
    --olive:#8a8a3c;
    --yellow:#f3e64b;
    --white:#ffffff;
    --ink:#141414;
    --ink-soft:#2a2a2a;
    --blue-text:#2f45d6;
    --green-text:#1f8a2a;
    --card-blue:#dfe3fb;
    --card-green:#dcefe4;
  }
  *{box-sizing:border-box;margin:0;padding:0}
  html,body{width:1050px;height:1200px;overflow:hidden}
  body{background:var(--stage);font-family:"Montserrat",sans-serif;position:relative}

  .page{position:absolute;top:214px;width:500px;height:772px;overflow:hidden;box-shadow:0 2px 10px rgba(0,0,0,.18)}
  .page--front{left:16px}
  .page--back{left:534px}
  .page-bg{position:absolute;inset:0}
  .abs{position:absolute}

  .wordmark{display:flex;align-items:center;gap:8px;white-space:nowrap}
  .wordmark__square{width:26px;height:26px;background:var(--ink)}
  .wordmark__name{font-family:"Bebas Neue",sans-serif;font-size:38px;line-height:1;color:var(--ink);letter-spacing:.5px}

  /* front */
  .front-logo{left:26px;top:26px}
  .front-headline{left:25px;top:122px;font-family:"Bebas Neue",sans-serif;font-size:42px;line-height:45px;color:var(--yellow)}
  .front-sub{left:25px;top:220px;width:420px;font-size:16.5px;line-height:21px;color:var(--white);font-weight:500}
  .front-body{left:25px;top:284px;width:448px;font-size:11px;line-height:15.2px;color:var(--white);text-align:justify}
  .front-body b{font-weight:700}
  .front-commit{left:80px;top:421px;width:394px;font-size:11px;line-height:15.2px;color:var(--white)}
  .front-photo{left:100px;top:486px;width:400px;height:214px}
  .front-cta{left:192px;top:708px;color:var(--white)}
  .front-cta__kicker{font-size:10px;letter-spacing:.3px}
  .front-cta__line{font-size:13px;font-weight:700;color:var(--yellow);margin-top:2px}

  /* back */
  .hero-title{left:31px;top:64px;font-family:"Bebas Neue",sans-serif;font-size:30px;line-height:38.5px;color:var(--yellow);white-space:nowrap;z-index:1}
  .hero-text{left:31px;top:187px;width:205px;font-size:10px;line-height:12.5px;font-weight:700;color:var(--white)}
  .hero-photo{left:250px;top:0;width:250px;height:280px}

  .plan{width:200px;border-radius:10px;padding:12px 14px}
  .plan--gpu{left:17px;top:284px;height:200px;background:var(--card-blue)}
  .plan--asic{left:17px;top:501px;height:198px;background:var(--card-green)}
  .plan__title{font-size:13px;font-weight:600;margin-bottom:10px}
  .plan--gpu .plan__title,.plan--gpu .plan__desc,.plan--gpu .plan__list{color:var(--blue-text)}
  .plan--asic .plan__title,.plan--asic .plan__desc,.plan--asic .plan__list{color:var(--green-text)}
  .plan__desc{font-size:8.6px;line-height:10.6px;margin-bottom:12px}
  .plan__list{list-style:none;font-size:8.6px;line-height:10.5px;font-weight:700}
  .plan__list li{position:relative;padding-left:15px;margin-bottom:11px}
  .plan__list li::before{content:"";position:absolute;left:1px;top:2px;width:5px;height:5px;border:1.5px solid currentColor;border-radius:50%}

  .features{left:246px;top:318px;width:234px;color:var(--ink-soft)}
  .features__heading{font-size:13px;line-height:16.5px;font-weight:600;color:var(--blue-text)}
  .features__text{font-size:9.6px;line-height:12px;margin-top:14px}
  .features__list{list-style:none;margin-top:12px;font-size:9.6px;line-height:12px;font-weight:700;color:var(--ink)}
  .features__list li{position:relative;padding-left:17px;margin-bottom:12px}
  .features__list li::before{content:"";position:absolute;left:2px;top:2px;width:5px;height:5px;border:1.5px solid var(--blue-text);border-radius:50%}
  .features__heading--gap{margin-top:24px}
  .features__term{font-size:9.6px;font-weight:700;color:var(--green-text);margin-top:11px}
  .features__def{font-size:9.6px}

  .footer-mark{left:104px;top:712px}
  .footer-mark .wordmark__square{width:18px;height:18px}
  .footer-mark .wordmark__name{font-size:24px}
  .footer-tag{left:104px;top:745px;font-size:8.4px;line-height:10.5px;font-weight:700;color:var(--white);white-space:nowrap}
  .footer-contact{left:318px;top:713px;font-size:8.4px;line-height:10.5px;color:var(--white);font-weight:500;white-space:nowrap}
  .footer-contact p+p{margin-top:12px}
</style>
</head>
<body>

<section class="page page--front">
  <svg class="page-bg" viewBox="0 0 500 772" aria-hidden="true">
    <rect width="500" height="772" fill="var(--lavender)"/>
    <polygon points="385,0 430,0 500,140 500,232" fill="var(--lavender-deep)"/>
    <polygon points="0,90 410,90 500,262 500,412 0,412" fill="var(--royal)"/>
    <rect y="412" width="500" height="360" fill="var(--night)"/>
    <polygon points="0,412 40,412 150,700 0,700" fill="var(--royal)" opacity=".9"/>
    <polygon points="0,530 55,530 118,700 0,700" fill="var(--teal)"/>
    <rect x="0" y="700" width="500" height="45" fill="var(--lavender)"/>
    <polygon points="0,708 95,708 110,728 0,728" fill="var(--olive)"/>
    <rect x="150" y="700" width="350" height="45" fill="var(--navy)" opacity=".85"/>
    <rect x="0" y="745" width="500" height="27" fill="var(--lavender)"/>
    <polygon points="340,745 500,745 500,772 355,772" fill="var(--olive)"/>
  </svg>

  <div class="abs wordmark front-logo">
    <span class="wordmark__square"></span>
    <span class="wordmark__name">Quarrytide Hosting</span>
  </div>

  <h1 class="abs front-headline">TRANSFORM MINING<br>WITH COHOSTING</h1>
  <p class="abs front-sub">Miners deserve the best - choose the hosting company that delivers excellence!</p>
  <p class="abs front-body">Quarrytide Hosting stands out in the industry by offering both GPU Hosting and ASIC Hosting services in our state-of-the-art facility, equipped with an impressive <b>17 Megawatts</b> of available power. What sets us apart is our unique billing system based on actual metered power usage. We charge <b>$0.08 for ASIC miners</b> and <b>$0.09</b> for <b>GPU miners</b>, ensuring cost-effectiveness and transparency for our clients.</p>

  <div class="abs front-photo" role="img" aria-label="Photo: miniature workers in orange vests handling a large gold bitcoin coin on a circuit board"
       style="background:radial-gradient(ellipse 40% 55% at 48% 42%,#c9b78a 0%,#7d7158 35%,#2b2d3a 70%,#14172a 100%)"></div>

  <p class="abs front-commit">Our commitment to excellence is evident in our use of cutting-edge technology, top-notch facilities, and strategic partnerships. These elements come together to deliver exceptional solutions tailored for real-world applications in the cryptocurrency space.</p>

  <div class="abs front-cta">
    <p class="front-cta__kicker">ARE YOU READY?</p>
    <p class="front-cta__line">Your Mining Success Story Begins Here</p>
  </div>
</section>

<section class="page page--back">
  <svg class="page-bg" viewBox="0 0 500 772" aria-hidden="true">
    <defs>
      <linearGradient id="heroFade" x1="0" y1="0" x2="0" y2="1">
        <stop offset="0" stop-color="#070a3a"/>
        <stop offset="1" stop-color="#0b1580"/>
      </linearGradient>
      <linearGradient id="sheetFade" x1="0" y1="0" x2="1" y2="1">
        <stop offset="0" stop-color="#eef0fb"/>
        <stop offset="1" stop-color="#c9d0f5"/>
      </linearGradient>
    </defs>
    <rect width="500" height="772" fill="url(#sheetFade)"/>
    <rect width="500" height="280" fill="url(#heroFade)"/>
    <rect y="704" width="500" height="68" fill="var(--royal)"/>
    <g stroke="var(--royal-soft)" stroke-width="1.5" fill="none" opacity=".8">
      <path d="M0 716 H40 L60 736 H90"/>
      <path d="M0 730 H30 L50 750 H80 L90 760"/>
      <path d="M10 772 L30 748 H70"/>
    </g>
  </svg>

  <div class="abs hero-photo" role="img" aria-label="Illustration: glowing gold bitcoin coin inside blue digital rings"
       style="background:radial-gradient(circle at 55% 48%,#f2b23a 0%,#c77b1c 22%,#1f7fe0 34%,#0b2a9a 52%,#070a3a 75%)"></div>
  <h2 class="abs hero-title">SOLUTIONS FOR EVERY<br>MINER, REGARDLESS<br>OF SCALE</h2>
  <p class="abs hero-text">Our solutions cater to cryptominers of all sizes, providing tailored options to meet diverse operational needs.</p>

  <div class="abs plan plan--gpu">
    <h3 class="plan__title">GPU Hosting</h3>
    <p class="plan__desc">Benefit from GPU hosting at an affordable rate of $0.09 per kilowatt-hour, ensurin cost-effective operations for your mining needs on any algorithm.</p>
    <ul class="plan__list">
      <li>One Time Setup Fee of $50 Per GPU Rig</li>
      <li>All-In $0.09 Per Kilowatt-Hour, No Additional Fees</li>
      <li>Remotely Monitor &amp; Access Your Equipment 24/7</li>
    </ul>
  </div>

  <div class="abs plan plan--asic">
    <h3 class="plan__title">ASIC Hosting</h3>
    <p class="plan__desc">Access ASIC hosting at a competitive rate of $0.08 per kilowatt-hour, ensuring efficient and cost-effective operations for your large scale mining endeavors.</p>
    <ul class="plan__list">
      <li>One Time Setup Fee of $50 Per ASIC Unit</li>
      <li>All-In $0.08 Per Kilowatt-Hour, No Additional Fees</li>
      <li>Remotely Monitor &amp; Access Your Equipment 24/7</li>
    </ul>
  </div>

  <div class="abs features">
    <h3 class="features__heading">Tailored Hosting Solutions For Every Individuals Need</h3>
    <p class="features__text">Quarrytide Hosting has committed to leveraging cutting-edge technology, state-of-the-art facilities, and strategic partnerships to deliver exceptional solutions tailored for real-world applications in the cryptocurrency space.</p>
    <ul class="features__list">
      <li>Insure Your Equipment, Safeguard Your Investment</li>
      <li>Utilize Our In House Tax Consultation To Your Advantage</li>
    </ul>
    <h3 class="features__heading features__heading--gap">Unleash The Power Of Scalability</h3>
    <p class="features__text">Unlock the potential for limitless growth with our scalable solutions. No more roadblocks, no more time constraints.</p>
    <p class="features__term">Scalability</p>
    <p class="features__def">Easily scale your operations</p>
    <p class="features__term">Cost Efficiency</p>
    <p class="features__def">Pay only for the resources you use</p>
  </div>

  <div class="abs wordmark footer-mark">
    <span class="wordmark__square"></span>
    <span class="wordmark__name">Quarrytide Hosting</span>
  </div>
  <p class="abs footer-tag">METERED, RELIABLE, SECURE -<br>MINERS DESERVE THE BEST HOSTING.</p>
  <div class="abs footer-contact">
    <p>Email us:<br>hello@quarrytidehosting.example</p>
    <p>Web:<br>quarrytidehosting.example</p>
  </div>
</section>

</body>
</html>
```